Bright Harbor Web Design & Marketing

Will award a 2nd place prize of $100.00 if someone can come up with a logo to match this design!
Updates

Okay, I'm really looking to see some better designs here. What do you think will bring the best designs out? Please remember with all future submissions I'm looking for a cartoon style / illustrator style website. I'm not sure what the technical term is for it, so I uploaded some images in the brief.

Target Market(s)

Small Business Owners

Industry/Entity Type

Marketing

Logo Text

BrightHarborly.com

Number of Pages Required

1 page

Colors

Designer to choose colors to be used in the design.

Requirements
Must have
• Logo should say BrightHarborly.com I would like more than just a text logo. I want some sort of cool custom graphic / icon with it that will look nice on shirts/hats/etc

```html
<!DOCTYPE html>
<html lang="en">
<head>
<meta charset="utf-8">
<title>BrightHarborly.com – Web Design &amp; Marketing</title>
<link href="https://fonts.googleapis.com/css2?family=Exo+2:wght@500;600;700;800&family=Open+Sans:ital,wght@0,400;0,600;0,700;1,400&display=swap" rel="stylesheet">
<style>
:root{
  --orange:#f26a10;
  --orange-dark:#d95a06;
  --ink:#222629;
  --text:#444a50;
  --muted:#7c8288;
  --line:#e1e3e5;
  --pale:#efefef;
  --nav:#2e3236;
  --dark:#1d2125;
  --white:#ffffff;
}
*{box-sizing:border-box;margin:0;padding:0}
html,body{width:1200px;height:4157px;overflow:hidden}
body{font-family:"Open Sans",Arial,sans-serif;color:var(--text);background:var(--white);position:relative}
.section-title{font-family:"Exo 2",Arial,sans-serif;font-weight:700;font-size:30px;color:var(--ink);text-align:center}
.section-title span{color:var(--orange)}
.section-title::after{content:"";display:block;width:46px;height:3px;background:var(--orange);margin:12px auto 0}

/* header */
.site-header{height:83px;border-top:5px solid var(--orange);display:flex;align-items:center;justify-content:space-between;padding:0 52px 0 145px}
.brand{font-family:"Exo 2",Arial,sans-serif;font-weight:800;font-size:29px;color:var(--orange);letter-spacing:.3px;display:flex;align-items:center;gap:10px}
.brand-dot{width:12px;height:12px;background:var(--orange);border-radius:50%}
.header-contact{display:flex;align-items:center;gap:22px}
.phone{display:flex;align-items:center;gap:10px;font-size:17px;color:var(--ink)}
.phone-icon{width:30px;height:30px;border:2px solid var(--orange);border-radius:50%;display:flex;align-items:center;justify-content:center}
.btn{display:inline-block;background:var(--orange);color:var(--white);font-size:14px;font-weight:600;border-radius:18px;padding:9px 22px}
.main-nav{height:39px;background:var(--nav);display:flex;padding-left:145px}
.main-nav a{color:var(--white);font-size:14px;font-weight:600;text-decoration:none;height:39px;line-height:39px;text-align:center}
.main-nav a.active{background:var(--orange)}

/* hero */
.hero{height:468px;position:relative;background:linear-gradient(100deg,#0d0f12 0%,#141a22 40%,#1e3552 70%,#0e1a29 100%)}
.hero-art{position:absolute;left:560px;top:0;width:640px;height:468px;background:radial-gradient(circle at 55% 55%,#5a88b8 0%,#2b4d74 30%,rgba(20,30,45,0) 70%)}
.hero h1{position:absolute;left:145px;top:160px;font-family:"Exo 2",Arial,sans-serif;font-weight:700;font-size:30px;line-height:40px;color:var(--white)}
.hero-dots{position:absolute;left:145px;top:300px;display:flex;gap:5px}
.hero-dots i{width:9px;height:9px;border-radius:50%;background:var(--white)}
.hero-dots i:first-child{background:var(--orange)}

/* about */
.about{height:269px;padding-top:63px;text-align:center}
.about .section-title::after{display:none}
.about p{width:910px;margin:20px auto 0;font-size:13.5px;line-height:21px;color:var(--text)}
.about p+p{margin-top:8px}

/* services */
.services{height:665px;background:var(--pale);padding-top:60px}
.service-grid{display:grid;grid-template-columns:repeat(3,288px);column-gap:25px;row-gap:25px;margin:42px 0 0 144px}
.service-card{height:142px;background:var(--white);border:1px solid var(--line);box-shadow:0 2px 5px rgba(0,0,0,.08);display:flex;padding:22px 16px 0 20px;gap:16px}
.service-card svg{flex:none}
.service-card h3{font-family:"Exo 2",Arial,sans-serif;font-size:17px;font-weight:600;line-height:20px;color:var(--ink)}
.service-card p{font-size:11.5px;line-height:16px;color:var(--muted);margin-top:8px}

/* call to action */
.cta{height:263px;background:linear-gradient(90deg,#1b1e22 0%,#33383e 50%,#1d2024 100%);text-align:center;padding-top:70px;color:var(--white)}
.cta p{width:900px;margin:0 auto;font-size:16px;line-height:25px}
.cta .btn{margin-top:28px;font-size:13px;padding:9px 26px}

/* difference */
.difference{height:369px;padding-top:58px}
.diff-row{display:flex;justify-content:center;gap:40px;margin-top:48px}
.diff-item{width:198px;text-align:center}
.diff-icon{width:78px;height:78px;margin:0 auto;border:3px solid var(--orange);border-radius:50%;display:flex;align-items:center;justify-content:center}
.diff-item h3{font-size:14px;font-weight:700;color:var(--ink);line-height:18px;margin-top:14px}
.diff-item p{font-size:11.5px;line-height:15px;color:var(--muted);margin-top:6px}

/* portfolio */
.portfolio{height:360px;background:var(--pale);padding-top:55px;position:relative}
.portfolio-row{display:flex;gap:25px;margin:40px 0 0 147px}
.portfolio-item{width:208px;height:150px;border:4px solid var(--white);box-shadow:0 2px 5px rgba(0,0,0,.12)}
.arrow{position:absolute;font-size:22px;color:#888}

/* team */
.team{height:637px;padding-top:58px;position:relative}
.team-row{display:flex;gap:22px;margin:34px 0 0 172px}
.team-card{width:155px;height:208px;border:1px solid var(--line);box-shadow:0 2px 5px rgba(0,0,0,.1);display:flex;flex-direction:column;align-items:center;background:var(--white)}
.team-photo{width:86px;height:86px;border-radius:50%;margin-top:14px;border:3px solid var(--white);box-shadow:0 0 0 1px var(--line)}
.team-card h3{font-size:13px;font-weight:700;color:var(--ink);margin-top:12px}
.team-card .role{font-size:11px;color:var(--muted);margin-top:2px}
.team-social{margin-top:auto;width:100%;height:38px;background:var(--nav);display:flex;justify-content:center;align-items:center;gap:6px}
.team-card.featured .team-social{background:var(--orange)}
.team-social i{width:20px;height:20px;border:1.5px solid var(--white);border-radius:50%}
.team-bio{width:912px;margin:32px 0 0 144px;border:1px solid var(--line);box-shadow:0 2px 6px rgba(0,0,0,.1);padding:20px 22px;text-align:center}
.team-bio p{font-size:12px;line-height:18px;color:var(--text)}
.team-bio p+p{margin-top:12px}

/* reviews */
.reviews{height:352px;background:var(--pale);padding-top:60px;position:relative}
.review-row{display:flex;gap:60px;margin:40px 0 0 144px}
.review{width:440px;display:flex;gap:18px}
.reviewer{width:80px;text-align:center;flex:none}
.avatar{width:70px;height:70px;border-radius:50%;margin:0 auto;border:3px solid var(--orange)}
.reviewer b{display:block;font-size:12px;color:var(--ink);margin-top:6px}
.stars{color:var(--orange);font-size:11px;letter-spacing:1px}
.review p{font-size:12px;line-height:17px;font-style:italic;color:var(--muted)}
.review-nav{position:absolute;left:144px;top:298px;width:912px;height:2px;background:var(--orange)}
.review-nav i{position:absolute;top:-8px;width:18px;height:18px;border-radius:50%;background:var(--orange)}
.review-nav i.off{background:var(--white);border:2px solid var(--line)}

/* clients */
.clients{height:286px;padding-top:62px;position:relative}
.client-row{display:flex;gap:17px;margin:38px 0 0 144px}
.client{width:138px;height:68px;background:var(--white);border:1px solid var(--line);box-shadow:0 2px 5px rgba(0,0,0,.1);display:flex;align-items:center;justify-content:center;font-family:"Open Sans",Arial,sans-serif;font-weight:700;font-size:17px;color:#333}

/* newsletter + footer */
.newsletter{height:61px;background:var(--orange);display:flex;align-items:center;padding-left:144px;gap:22px}
.newsletter h2{font-family:"Exo 2",Arial,sans-serif;font-weight:700;font-size:24px;color:var(--white);width:300px}
.news-form{display:flex;margin-left:14px}
.news-form span{width:425px;height:30px;background:var(--white);font-size:11px;color:#999;line-height:30px;padding-left:12px}
.news-form b{width:118px;height:30px;background:var(--dark);color:var(--white);font-size:12px;line-height:30px;text-align:center}
.site-footer{height:277px;background:linear-gradient(180deg,#262a2f,#17191c);position:relative;color:var(--white);display:flex;padding:24px 0 0 144px}
.footer-col h4{font-size:13px;font-weight:700;margin-bottom:14px}
.footer-col li{list-style:none;font-size:11.5px;line-height:20px;padding-left:12px;position:relative}
.footer-col li::before{content:"›";position:absolute;left:0}
.links{width:210px}
.contact{width:236px}
.contact div{display:flex;gap:10px;font-size:11px;line-height:15px;margin-bottom:12px}
.contact svg{flex:none}
.inquiry{width:270px}
.inquiry span{display:block;width:195px;height:24px;background:var(--white);color:#999;font-size:10px;line-height:24px;padding-left:6px;margin-bottom:8px}
.inquiry span.msg{height:46px}
.inquiry b{display:inline-block;background:var(--orange);font-size:10px;padding:4px 14px;border-radius:10px}
.footer-brand{padding-top:74px}
.footer-brand .brand{font-size:21px;color:var(--white)}
.footer-brand .brand-dot{background:var(--white);width:9px;height:9px}
.footer-social{display:flex;gap:8px;margin:14px 0 0 36px}
.footer-social i{width:22px;height:22px;border-radius:50%;background:#3a78c2}
.footer-social i:last-child{background:#d84a3a}
.copyright{height:28px;background:#101214;color:#bbb;font-size:11px;text-align:center;line-height:28px}
</style>
</head>
<body>

<header class="site-header">
  <div class="brand"><span class="brand-dot"></span>BrightHarborly.com</div>
  <div class="header-contact">
    <div class="phone">
      <span class="phone-icon"><svg width="14" height="14" viewBox="0 0 24 24"><path d="M6 2l4 4-2 3c1 3 4 6 7 7l3-2 4 4-3 4C10 22 2 14 2 5z" fill="#f26a10"/></svg></span>
      123.456.7890
    </div>
    <span class="btn">Contact Us Now</span>
  </div>
</header>
<nav class="main-nav">
  <a class="active" style="width:125px">Home</a>
  <a style="width:190px">Services &amp; Pricing</a>
  <a style="width:170px">Our Team</a>
  <a style="width:200px">Clients/portfolio</a>
  <a style="width:170px">Contact Us</a>
</nav>

<section class="hero">
  <div class="hero-art" role="img" aria-label="Hand holding a glowing network of connected digital icons above a laptop"></div>
  <h1>The Design &amp; Marketing Team<br>That Always Puts Trust &amp; Loyalty<br>Before Profits</h1>
  <div class="hero-dots"><i></i><i></i><i></i></div>
</section>

<section class="about">
  <h2 class="section-title">About <span>BrightHarborly</span>.com</h2>
  <p>We believe that honesty and integrity come before personal profits. We are a family owned and operated company. Our parents raised us to take care of each other and that's exactly what we've done. We treat each of our clients with the same loyalty and respect that we give each other.</p>
  <p>We are not looking to have hundreds and hundreds of clients. We are looking to expand our family with a handful of like-minded individuals. Companies who take pride in their work and their customers. We want to build mutually beneficial, lucrative, and long term partnerships.</p>
</section>

<section class="services">
  <h2 class="section-title">Our <span>Services</span></h2>
  <div class="service-grid">
    <div class="service-card"><svg width="50" height="46" viewBox="0 0 50 46"><rect x="3" y="4" width="44" height="30" rx="2" fill="none" stroke="#f26a10" stroke-width="4"/><rect x="20" y="34" width="10" height="6" fill="#f26a10"/><rect x="13" y="40" width="24" height="4" fill="#f26a10"/></svg><div><h3>Website Design<br>&amp; Management</h3><p>Lorem ipsum dolor sit amet, consetuer adipiscing elit, sed diam nonummy nibh euismod tincidunt ut laoreet.</p></div></div>
    <div class="service-card"><svg width="50" height="46" viewBox="0 0 50 46"><rect x="4" y="4" width="32" height="38" rx="2" fill="none" stroke="#f26a10" stroke-width="4"/><rect x="11" y="12" width="10" height="10" fill="#f26a10"/><rect x="11" y="28" width="18" height="3" fill="#f26a10"/><path d="M38 8l8 8-14 22-6 2 2-6z" fill="#f26a10"/></svg><div><h3>Logo Design<br>&amp; Branding Materials</h3><p>Lorem ipsum dolor sit amet, consetuer adipiscing elit, sed diam nonummy nibh euismod tincidunt ut laoreet.</p></div></div>
    <div class="service-card"><svg width="50" height="46" viewBox="0 0 50 46"><path d="M8 6h34l5 14H3z" fill="#f26a10"/><rect x="6" y="22" width="38" height="20" fill="none" stroke="#f26a10" stroke-width="4"/><rect x="19" y="28" width="12" height="14" fill="#f26a10"/></svg><div><h3>Online Store Design<br>&amp; Management</h3><p>Lorem ipsum dolor sit amet, consetuer adipiscing elit, sed diam nonummy nibh euismod tincidunt ut laoreet.</p></div></div>
    <div class="service-card"><svg width="50" height="46" viewBox="0 0 50 46"><path d="M25 3a14 14 0 0 1 14 14c0 11-14 26-14 26S11 28 11 17A14 14 0 0 1 25 3z" fill="none" stroke="#f26a10" stroke-width="4"/><circle cx="25" cy="17" r="5" fill="#f26a10"/></svg><div><h3>Local<br>SEO Management</h3><p>Lorem ipsum dolor sit amet, consetuer adipiscing elit, sed diam nonummy nibh euismod tincidunt ut laoreet.</p></div></div>
    <div class="service-card"><svg width="50" height="46" viewBox="0 0 50 46"><circle cx="20" cy="19" r="14" fill="none" stroke="#f26a10" stroke-width="4"/><path d="M30 29l14 14" stroke="#f26a10" stroke-width="6" stroke-linecap="round"/><path d="M13 23l5-5 4 3 6-7" fill="none" stroke="#f26a10" stroke-width="3"/></svg><div><h3>Search Engine<br>Optimization</h3><p>Lorem ipsum dolor sit amet, consetuer adipiscing elit, sed diam nonummy nibh euismod tincidunt ut laoreet.</p></div></div>
    <div class="service-card"><svg width="50" height="46" viewBox="0 0 50 46"><circle cx="25" cy="23" r="19" fill="#f26a10"/><circle cx="25" cy="23" r="6" fill="#fff"/><circle cx="14" cy="14" r="3" fill="#fff"/><circle cx="36" cy="14" r="3" fill="#fff"/><circle cx="25" cy="36" r="3" fill="#fff"/></svg><div><h3>Social Media<br>Marketing</h3><p>Lorem ipsum dolor sit amet, consetuer adipiscing elit, sed diam nonummy nibh euismod tincidunt ut laoreet.</p></div></div>
    <div class="service-card"><svg width="50" height="46" viewBox="0 0 50 46"><rect x="3" y="10" width="30" height="26" fill="none" stroke="#f26a10" stroke-width="4"/><rect x="22" y="4" width="24" height="20" fill="#f26a10"/><rect x="9" y="28" width="16" height="3" fill="#f26a10"/></svg><div><h3>Marketing<br>Material &amp; Print Design</h3><p>Lorem ipsum dolor sit amet, consetuer adipiscing elit, sed diam nonummy nibh euismod tincidunt ut laoreet.</p></div></div>
    <div class="service-card"><svg width="50" height="46" viewBox="0 0 50 46"><circle cx="25" cy="24" r="12" fill="#f26a10"/><circle cx="25" cy="24" r="18" fill="none" stroke="#f26a10" stroke-width="3" stroke-dasharray="6 4"/><circle cx="25" cy="24" r="4" fill="#fff"/></svg><div><h3>Outsourcing<br>Management</h3><p>Lorem ipsum dolor sit amet, consetuer adipiscing elit, sed diam nonummy nibh euismod tincidunt ut laoreet.</p></div></div>
    <div class="service-card"><svg width="50" height="46" viewBox="0 0 50 46"><circle cx="12" cy="14" r="6" fill="#f26a10"/><circle cx="38" cy="14" r="6" fill="#f26a10"/><rect x="4" y="22" width="16" height="16" rx="3" fill="#f26a10"/><rect x="30" y="22" width="16" height="16" rx="3" fill="#f26a10"/><rect x="14" y="30" width="22" height="4" fill="#f26a10"/></svg><div><h3>Consulting<br>Service</h3><p>Lorem ipsum dolor sit amet, consetuer adipiscing elit, sed diam nonummy nibh euismod tincidunt ut laoreet.</p></div></div>
  </div>
</section>

<section class="cta" role="img" aria-label="Dimmed photo of a desk workspace behind the call to action">
  <p>Lorem ipsum dolor sit amet, consectetuer adipiscing elit, sed diam nonummy nibh euismod tincidunt ut laoreet dolore magna aliquam erat volutpat. Ut wisi enim ad minim veniam, quis nostrud exerci tation ullamcorper.</p>
  <span class="btn">CONTACT US NOW</span>
</section>

<section class="difference">
  <h2 class="section-title">What Makes <span>Me Different?</span></h2>
  <div class="diff-row">
    <div class="diff-item"><div class="diff-icon"><svg width="36" height="34" viewBox="0 0 36 34"><path d="M18 3L34 31H2z" fill="none" stroke="#f26a10" stroke-width="3"/><rect x="16.5" y="12" width="3" height="10" fill="#f26a10"/><rect x="16.5" y="25" width="3" height="3" fill="#f26a10"/></svg></div><h3>100% Risk Free<br>Investment</h3><p>If we are unable to deliver anything that we say we can we will refund you 100% of your investment.</p></div>
    <div class="diff-item"><div class="diff-icon"><svg width="38" height="28" viewBox="0 0 38 28"><rect x="2" y="2" width="34" height="24" rx="3" fill="none" stroke="#f26a10" stroke-width="3"/><rect x="2" y="8" width="34" height="5" fill="#f26a10"/><rect x="7" y="18" width="10" height="3" fill="#f26a10"/></svg></div><h3>Customer Loyalty<br>Program</h3><p>After 12 months of on time payments – Customers will receive cash back reward bonuses.</p></div>
    <div class="diff-item"><div class="diff-icon"><svg width="34" height="36" viewBox="0 0 34 36"><rect x="2" y="2" width="30" height="32" rx="4" fill="#f26a10"/><circle cx="17" cy="14" r="5" fill="#fff"/><path d="M8 29c1-6 5-8 9-8s8 2 9 8z" fill="#fff"/></svg></div><h3>Unmatched Personal<br>Service</h3><p>Do you need us to come to your office to help train staff on the management of your new...</p></div>
    <div class="diff-item"><div class="diff-icon"><svg width="38" height="28" viewBox="0 0 38 28"><rect x="2" y="2" width="34" height="24" rx="3" fill="#f26a10"/><rect x="2" y="7" width="34" height="4" fill="#fff"/><rect x="24" y="16" width="8" height="5" fill="#fff"/></svg></div><h3>Multiple Payment<br>Options Available</h3><p>Website Leasing, 90 Days Same As Cash, Website Financing.</p></div>
  </div>
</section>

<section class="portfolio">
  <h2 class="section-title">Work <span>Portfolio</span></h2>
  <span class="arrow" style="left:98px;top:182px">‹</span>
  <span class="arrow" style="left:1090px;top:182px">›</span>
  <div class="portfolio-row">
    <div class="portfolio-item" style="background:linear-gradient(135deg,#f4f4f4,#c9c9c9)" role="img" aria-label="Website layout mockup with photo of a person"></div>
    <div class="portfolio-item" style="background:linear-gradient(135deg,#2f5fa8,#e9832c)" role="img" aria-label="Blue and orange stationery branding set"></div>
    <div class="portfolio-item" style="background:linear-gradient(135deg,#5a5a5a,#3a3a3a)" role="img" aria-label="Dark logo presentation, labelled Laoreet Dolore Magna"></div>
    <div class="portfolio-item" style="background:linear-gradient(135deg,#21a3b6,#1a8c9c)" role="img" aria-label="Teal illustration of a laptop surrounded by marketing icons"></div>
  </div>
</section>

<section class="team">
  <h2 class="section-title">Our <span>Team</span></h2>
  <span class="arrow" style="left:94px;top:252px;font-size:16px">‹</span>
  <span class="arrow" style="left:1094px;top:252px;font-size:16px">›</span>
  <div class="team-row">
    <div class="team-card featured"><div class="team-photo" style="background:linear-gradient(#d9c4b4,#8a5a48)" role="img" aria-label="Portrait of team member"></div><h3>Marcus Hale</h3><div class="role">Chief Executive Officer</div><div class="team-social"><i></i><i></i><i></i></div></div>
    <div class="team-card"><div class="team-photo" style="background:linear-gradient(#cfd3d7,#4e5660)" role="img" aria-label="Portrait of team member"></div><h3>Marcus Hale</h3><div class="role">Chief Operations Officer</div><div class="team-social"><i></i><i></i><i></i></div></div>
    <div class="team-card"><div class="team-photo" style="background:linear-gradient(#e6d8cc,#6b4c3c)" role="img" aria-label="Portrait of team member"></div><h3>Marcus Hale</h3><div class="role">Chief Technical Officer</div><div class="team-social"><i></i><i></i><i></i></div></div>
    <div class="team-card"><div class="team-photo" style="background:linear-gradient(#f0e6d8,#c9a884)" role="img" aria-label="Portrait of team member"></div><h3>Marcus Hale</h3><div class="role">Finance</div><div class="team-social"><i></i><i></i><i></i></div></div>
    <div class="team-card"><div class="team-photo" style="background:linear-gradient(#dcdfe3,#3e4650)" role="img" aria-label="Portrait of team member"></div><h3>Marcus Hale</h3><div class="role">Chief Executive Officer</div><div class="team-social"><i></i><i></i><i></i></div></div>
  </div>
  <div class="team-bio">
    <p>Lorem ipsum dolor sit amet, consectetuer adipiscing elit, sed diam nonummy nibh euismod tincidunt ut laoreet dolore magna aliquam erat volutpat. Ut wisi enim ad minim veniam, quis nostrud exerci tation ullamcorper suscipit lobortis nisl ut aliquip ex ea commodo consequat. Duis autem vel eum iriure dolor in hendrerit in vulputate velit esse molestie consequat, vel illum dolore eu feugiat nulla facilisis at vero eros et accumsan et iusto odio dignissim qui blandit praesent luptatum zzril delenit augue duis dolore te feugait nulla facilisi.</p>
    <p>Lorem ipsum dolor sit amet, consectetuer adipiscing elit, sed diam nonummy nibh euismod tincidunt ut laoreet dolore magna aliquam erat volutpat. Ut wisi enim ad minim veniam, quis nostrud exerci tation ullamcorper suscipit lobortis nisl ut aliquip ex ea commodo consequat. Duis autem vel eum iriure dolor in hendrerit in vulputate velit esse molestie consequat, vel illum dolore eu feugiat nulla facilisis at vero eros et accumsan et iusto odio dignissim qui blandit praesent luptatum zzril delenit augue duis dolore te feugait nulla facilisi.</p>
  </div>
</section>

<section class="reviews">
  <h2 class="section-title">Client <span>Reviews</span></h2>
  <div class="review-row">
    <div class="review"><div class="reviewer"><div class="avatar" style="background:linear-gradient(#e4e6e8,#6a727a)" role="img" aria-label="Client avatar"></div><b>Lorem ipsum</b><div class="stars">★★★★☆</div></div><p>“ Lorem ipsum sit amet as adipiscitasdahd essit nu mod dhaqor incidunt ut la dolore ma aliquamera molit enim ad mini veniam. Exercitation ullamco quis nostrud exercit tation ullamcorper suscipit lobortis nisl ut aliquip. Accusant doloremque inventore veritatis quasi beatae facilisis doloremque. ”</p></div>
    <div class="review"><div class="reviewer"><div class="avatar" style="background:linear-gradient(#e4e6e8,#6a727a)" role="img" aria-label="Client avatar"></div><b>Lorem ipsum</b><div class="stars">★★★★☆</div></div><p>“ Lorem ipsum sit amet as adipiscitasdahd essit nu mod dhaqor incidunt ut la dolore ma aliquamera molit enim ad mini veniam. Exercitation ullamco quis nostrud exercit tation ullamcorper suscipit lobortis nisl ut aliquip. Accusant doloremque inventore veritatis quasi beatae facilisis doloremque. ”</p></div>
  </div>
  <div class="review-nav"><i class="off" style="left:432px"></i><i style="left:458px"></i></div>
</section>

<section class="clients">
  <h2 class="section-title">Our <span>Clients</span></h2>
  <span class="arrow" style="left:100px;top:172px">‹</span>
  <span class="arrow" style="left:1086px;top:172px">›</span>
  <div class="client-row">
    <div class="client">WESTROW</div>
    <div class="client">pathline</div>
    <div class="client">Kellgrove</div>
    <div class="client">Novaris</div>
    <div class="client">ARCHfield</div>
    <div class="client">pathline</div>
  </div>
</section>

<section class="newsletter">
  <svg width="36" height="30" viewBox="0 0 36 30"><rect x="2" y="4" width="32" height="22" fill="#fff"/><path d="M2 4l16 12L34 4" fill="none" stroke="#f26a10" stroke-width="2.5"/></svg>
  <h2>Subscribe Our Newsletter</h2>
  <div class="news-form"><span>Enter Your Email Address</span><b>SUBSCRIBE »</b></div>
</section>

<footer class="site-footer" role="img" aria-label="Dark city skyline at night behind the footer">
  <div class="footer-col links">
    <h4>Quick Links</h4>
    <ul><li>Home</li><li>SERVICES &amp; PRICING</li><li>OUR TEAM</li><li>CLIENTS/PORTFOLIO</li><li>Contact Us</li></ul>
  </div>
  <div class="footer-col contact">
    <h4>Contact Details</h4>
    <div><svg width="12" height="16" viewBox="0 0 12 16"><path d="M6 0a6 6 0 0 1 6 6c0 4-6 10-6 10S0 10 0 6a6 6 0 0 1 6-6z" fill="#fff"/><circle cx="6" cy="6" r="2" fill="#222"/></svg><span>BrightHarborly.com<br>0907 Lorem ipsum dolor<br>sit amet adipiscing</span></div>
    <div><svg width="12" height="12" viewBox="0 0 24 24"><path d="M6 2l4 4-2 3c1 3 4 6 7 7l3-2 4 4-3 4C10 22 2 14 2 5z" fill="#fff"/></svg><span>123.456.7890</span></div>
    <div><svg width="12" height="12" viewBox="0 0 24 24"><path d="M6 2l4 4-2 3c1 3 4 6 7 7l3-2 4 4-3 4C10 22 2 14 2 5z" fill="#fff"/></svg><span>123.456.7890</span></div>
    <div><svg width="13" height="10" viewBox="0 0 13 10"><rect width="13" height="10" fill="#fff"/><path d="M0 0l6.5 5L13 0" fill="none" stroke="#222"/></svg><span>info@BrightHarborly.com</span></div>
  </div>
  <div class="footer-col inquiry">
    <h4>Quick Inquiry</h4>
    <span>Name</span><span>Email</span><span class="msg">Message</span><b>SUBMIT</b>
  </div>
  <div class="footer-brand">
    <div class="brand"><span class="brand-dot"></span>BrightHarborly.com</div>
    <div class="footer-social"><i></i><i></i><i></i><i></i></div>
  </div>
</footer>
<div class="copyright">Copyright © 2017 BrightHarborly.com. All Rights Reserved.</div>

</body>
</html>
```